I need a full PowerPoint template (with multiple slide options) for a new imaging center company - Lumora Medical Imaging. I have attached the Logo and Brand Identity here.

```html
<!DOCTYPE html>
<html lang="en">
<head>
<meta charset="utf-8">
<title>Lumora Medical Imaging – Presentation Template</title>
<link href="https://fonts.googleapis.com/css2?family=Poppins:ital,wght@0,400;0,500;0,600;0,700;0,800;1,400&display=swap" rel="stylesheet">
<style>
:root{
  --navy:#1f1b5c;
  --green:#1e9a4a;
  --blue:#1a7cc5;
  --sky:#8ec5ea;
  --ink:#222;
  --grey:#8a8a95;
  --board:#d6d9dd;
  --paper:#ffffff;
}
*{margin:0;padding:0;box-sizing:border-box}
html,body{width:883px;height:1200px;overflow:hidden}
body{background:var(--board);font-family:'Poppins',sans-serif;color:var(--ink);position:relative}
.slide{position:absolute;width:265px;height:149px;background:var(--paper);overflow:hidden;box-shadow:1px 2px 4px rgba(0,0,0,.18)}
.abs{position:absolute}
.heading{position:absolute;left:9px;top:8px;font-size:9px;color:var(--navy);font-weight:400;white-space:nowrap}
.heading b{font-weight:700}
.heading::after{content:"";position:absolute;left:0;top:15px;width:20px;height:2px;background:var(--green);border-radius:1px}
.corner-dot{position:absolute;right:8px;top:6px;width:12px;height:12px;border-radius:50%;background:var(--blue);border:2px solid var(--green)}
.footer{position:absolute;left:10px;bottom:4px;font-size:4.5px;font-weight:700;color:var(--navy);letter-spacing:.2px}
.footer-line{position:absolute;left:36px;right:10px;bottom:6px;height:.5px;background:#c9c9d2}
.page-no{position:absolute;right:6px;bottom:4px;font-size:3px;color:var(--grey)}
.tx{font-size:2.6px;line-height:1.45;color:var(--grey)}
.ttl{font-size:4.5px;font-weight:700;color:var(--navy);line-height:1.2}
.ttl span{color:var(--green)}
.photo{position:absolute;border-radius:4px}
.brand{font-weight:700;color:var(--navy);white-space:nowrap;display:flex;align-items:center;gap:4px}
.brand i{display:inline-block;border-radius:50%;background:var(--blue);flex:none}
.brand-name{display:flex;flex-direction:column;line-height:1}
.brand-name small{font-size:.42em;letter-spacing:.6px;margin-top:1.5px}
</style>
</head>
<body>

<!-- Row 1 -->
<section class="slide cover-a" style="left:30px;top:35px">
  <svg class="abs" style="left:0;top:0" width="265" height="149" viewBox="0 0 265 149">
    <circle cx="205" cy="70" r="92" fill="var(--blue)"/>
    <circle cx="205" cy="70" r="78" fill="#fff"/>
    <path d="M265 95 A92 92 0 0 1 190 149 L265 149 Z" fill="var(--navy)"/>
  </svg>
  <div class="photo" role="img" aria-label="Smiling female doctor holding a clipboard" style="left:140px;top:0;width:105px;height:149px;border-radius:0;background:linear-gradient(180deg,#e9eef3,#cfd8e2 60%,#eef2f6)"></div>
  <div class="abs" style="left:5px;top:5px;width:6px;height:6px;background:var(--navy)"></div>
  <div class="abs brand" style="left:15px;top:29px;font-size:12px"><i style="width:20px;height:20px"></i><span class="brand-name">LUMORA<small>MEDICAL IMAGING</small></span></div>
  <div class="abs" style="left:15px;top:69px;font-size:14px;font-weight:700;color:var(--navy);line-height:1">Business</div>
  <div class="abs" style="left:15px;top:84px;font-size:17px;font-weight:700;color:var(--green);line-height:1">Marketing</div>
  <div class="abs" style="left:15px;top:112px;font-size:6px;font-weight:600;color:var(--blue)">Presentation Template</div>
  <div class="abs tx" style="left:15px;top:120px;width:90px;color:#555">Lorem ipsum is simply sample text of the printing and layout trade.</div>
</section>

<section class="slide cover-b" style="left:312px;top:35px">
  <div class="abs" style="left:6px;top:5px;width:6px;height:6px;background:var(--blue)"></div>
  <div class="abs brand" style="left:15px;top:27px;font-size:11px"><i style="width:18px;height:18px"></i><span class="brand-name">LUMORA<small>MEDICAL IMAGING</small></span></div>
  <div class="abs" style="left:16px;top:66px;font-size:16px;font-weight:700;color:var(--green);line-height:1">Business</div>
  <div class="abs" style="left:16px;top:83px;font-size:12px;font-weight:700;color:var(--navy);line-height:1">Marketing</div>
  <div class="abs" style="left:16px;top:103px;font-size:6.5px;font-weight:500;color:var(--blue)">Presentation</div>
  <div class="abs tx" style="left:16px;top:112px;width:75px;font-style:italic">Lorem ipsum dolor sit amet, consectetuer adipiscing elit, sed diam nonum</div>
  <div class="abs" style="left:16px;top:133px;display:flex;gap:3px"><i style="width:3px;height:3px;border-radius:50%;background:var(--navy)"></i><i style="width:3px;height:3px;border-radius:50%;background:var(--navy)"></i><i style="width:3px;height:3px;border-radius:50%;background:var(--green)"></i></div>
  <div class="photo" role="img" aria-label="Smiling male doctor with glasses and stethoscope in a bright clinic" style="left:111px;top:0;width:154px;height:121px;border-radius:0;background:linear-gradient(135deg,#dfe7ee,#f2f5f8 50%,#c8d3de)"></div>
  <div class="abs" style="left:111px;top:121px;width:154px;height:28px;background:var(--navy);color:#fff;font-size:5px;letter-spacing:1.6px;text-align:center;line-height:28px">www.lumoraimaging.com</div>
</section>

<section class="slide toc" style="left:591px;top:35px">
  <div class="abs" style="left:11px;top:7px;font-size:10px;color:var(--navy)">Table of <b>Contents</b></div>
  <div class="abs" style="left:11px;top:22px;width:20px;height:2px;background:var(--green)"></div>
  <div class="corner-dot"></div>
  <svg class="abs" style="left:0;top:0" width="265" height="149" viewBox="0 0 265 149" font-family="Poppins, sans-serif">
    <g font-size="4" font-weight="600" fill="var(--navy)">
      <text x="30" y="50">Simple Text One</text><text x="30" y="65">Simple Text Two</text><text x="30" y="81">Simple Text Three</text><text x="30" y="96">Simple Text Four</text><text x="30" y="111">Simple Text Five</text>
      <text x="145" y="50">Simple Text One</text><text x="145" y="65">Simple Text Two</text><text x="145" y="81">Simple Text Three</text><text x="145" y="96">Simple Text Four</text><text x="145" y="111">Simple Text Five</text>
    </g>
    <g fill="var(--green)">
      <circle cx="27" cy="48.6" r="1"/><circle cx="27" cy="63.6" r="1"/><circle cx="27" cy="79.6" r="1"/><circle cx="27" cy="94.6" r="1"/><circle cx="27" cy="109.6" r="1"/>
      <circle cx="142" cy="48.6" r="1"/><circle cx="142" cy="63.6" r="1"/><circle cx="142" cy="79.6" r="1"/><circle cx="142" cy="94.6" r="1"/><circle cx="142" cy="109.6" r="1"/>
    </g>
    <g stroke="#9a9aa8" stroke-width=".4">
      <path d="M30 51.5H117M30 66.5H117M30 82.5H117M30 97.5H117M30 112.5H117M145 51.5H232M145 66.5H232M145 82.5H232M145 97.5H232M145 112.5H232"/>
    </g>
    <g fill="var(--navy)">
      <circle cx="121" cy="51.5" r="3.5"/><circle cx="121" cy="66.5" r="3.5"/><circle cx="121" cy="82.5" r="3.5"/><circle cx="121" cy="97.5" r="3.5"/><circle cx="121" cy="112.5" r="3.5"/>
      <circle cx="236" cy="51.5" r="3.5"/><circle cx="236" cy="66.5" r="3.5"/><circle cx="236" cy="82.5" r="3.5"/><circle cx="236" cy="97.5" r="3.5"/><circle cx="236" cy="112.5" r="3.5"/>
    </g>
    <g fill="#fff" font-size="2.8" font-weight="600" text-anchor="middle">
      <text x="121" y="52.5">02</text><text x="121" y="67.5">04</text><text x="121" y="83.5">06</text><text x="121" y="98.5">08</text><text x="121" y="113.5">10</text>
      <text x="236" y="52.5">02</text><text x="236" y="67.5">04</text><text x="236" y="83.5">06</text><text x="236" y="98.5">08</text><text x="236" y="113.5">10</text>
    </g>
  </svg>
  <div class="footer">LUMORA</div><div class="footer-line"></div><div class="page-no">2</div>
</section>

<!-- Row 2 -->
<section class="slide mission" style="left:30px;top:198px">
  <div class="heading"><b>Heading</b> Goes Here</div><div class="corner-dot"></div>
  <div class="abs tx" style="left:17px;top:31px;width:112px;font-size:3.8px;font-style:italic;color:#444">Lorem ipsum dolor sit amet, cons ectetuer adipiscing elit, sed diam nonummy nibh euismod tincidunt. Lorem ipsum dolor sit amet.</div>
  <div class="photo" role="img" aria-label="Presenter at a whiteboard with colleagues in a meeting room" style="left:17px;top:58px;width:109px;height:64px;background:linear-gradient(135deg,#b9c4cf,#e8ecef 55%,#5d6470)"></div>
  <div class="abs" style="left:142px;top:47px;width:22px;height:25px;border-radius:3px;background:var(--blue)"></div>
  <div class="abs" style="left:170px;top:48px;font-size:6px;font-weight:700;color:var(--navy)">Our <span style="color:var(--blue)">Mission</span></div>
  <div class="abs tx" style="left:170px;top:56px;width:70px;font-style:italic">Lorem ipsum dolor sit amet, cons ectetuer adipiscing elit, sed diam nonummy nibh euismod tincidunt.</div>
  <div class="abs" style="left:142px;top:89px;width:22px;height:25px;border-radius:3px;background:var(--blue)"></div>
  <div class="abs" style="left:170px;top:90px;font-size:6px;font-weight:700;color:var(--navy)">Our <span style="color:var(--blue)">Vision</span></div>
  <div class="abs tx" style="left:170px;top:98px;width:70px;font-style:italic">Lorem ipsum dolor sit amet, cons ectetuer adipiscing elit, sed diam nonummy nibh euismod tincidunt.</div>
  <div class="footer">LUMORA</div><div class="footer-line"></div><div class="page-no">3</div>
</section>

<section class="slide process" style="left:312px;top:198px">
  <div class="heading"><b>Heading</b> Goes Here</div><div class="corner-dot"></div>
  <svg class="abs" style="left:0;top:0" width="265" height="149" viewBox="0 0 265 149">
    <g fill="none" stroke="var(--navy)" stroke-width="1.4">
      <path d="M54 33H90Q95 33 95 38V46M95 52V97Q95 102 90 102H54Q50 102 50 97V38Q50 33 54 33"/>
      <path d="M115 33H151Q156 33 156 38V46M156 52V97Q156 102 151 102H115Q111 102 111 97V52M111 46V38Q111 33 115 33"/>
      <path d="M176 33H212Q217 33 217 38V97Q217 102 212 102H176Q172 102 172 97V52M172 46V38Q172 33 176 33"/>
      <path d="M95 49H111M156 49H172"/>
    </g>
    <g fill="var(--navy)"><circle cx="95" cy="49" r="1.8"/><circle cx="156" cy="49" r="1.8"/></g>
    <g fill="none" stroke="var(--green)" stroke-width=".8">
      <circle cx="72.5" cy="46" r="2.5"/><rect x="130" y="44" width="7" height="5"/><path d="M130 44l3.5 3 3.5-3M191 43v6h7M192 47l2-2 2 1 2-2"/>
    </g>
    <g font-family="Poppins, sans-serif" font-size="4" font-weight="700" fill="var(--blue)" text-anchor="middle">
      <text x="72.5" y="58">IDEA</text><text x="133.5" y="58">PROMOTION</text><text x="194.5" y="58">GROWTH</text>
    </g>
  </svg>
  <div class="abs tx" style="left:56px;top:62px;width:34px;text-align:center">Lorem ipsum dolor sit amet, consectetuer adipiscing elit, sed diam nonummy nibh euismod tincidunt ut laoreet dolore magna aliquam erat.</div>
  <div class="abs tx" style="left:117px;top:62px;width:34px;text-align:center">Lorem ipsum dolor sit amet, consectetuer adipiscing elit, sed diam nonummy nibh euismod tincidunt ut laoreet dolore magna aliquam erat.</div>
  <div class="abs tx" style="left:178px;top:62px;width:34px;text-align:center">Lorem ipsum dolor sit amet, consectetuer adipiscing elit, sed diam nonummy nibh euismod tincidunt ut laoreet dolore magna aliquam erat.</div>
  <div class="abs tx" style="left:34px;top:110px;width:198px;text-align:center;color:#555">Lorem ipsum dolor sit amet, consectetuer adipiscing elit, sed diam nonummy nibh euismod tincidunt ut laoreet dolore magna aliquam erat volutpat. Ut wisi enim ad minim veniam, quis nostrud exerci tation ullamcorper suscipit lobortis nisl ut aliquip ex ea commodo consequat.</div>
  <div class="footer">LUMORA</div><div class="footer-line"></div><div class="page-no">4</div>
</section>

<section class="slide photo-points" style="left:591px;top:198px">
  <div class="heading"><b>Heading</b> Goes Here</div><div class="corner-dot"></div>
  <div class="photo" role="img" aria-label="Doctor holding a tablet with glowing digital health icons" style="left:28px;top:31px;width:88px;height:92px;background:linear-gradient(150deg,#dceaf4,#8fc1e2 50%,#e3eef6)"></div>
  <div class="abs" style="left:127px;top:31px;width:113px">
    <div class="ttl" style="font-size:5.5px"><span>01.</span> Text Added Here</div>
    <div class="tx" style="margin:2px 0 8px">Lorem ipsum dolor sit amet, consectetuer adipiscing elit, sed diam nonummy nibh euismod tincidunt ut laoreet dolore magna aliquam erat volutpat. Ut wisi enim ad minim veniam.</div>
    <div class="ttl" style="font-size:5.5px"><span>02.</span> Text Added Here</div>
    <div class="tx" style="margin:2px 0 8px">Lorem ipsum dolor sit amet, consectetuer adipiscing elit, sed diam nonummy nibh euismod tincidunt ut laoreet dolore magna aliquam erat volutpat. Ut wisi enim ad minim veniam.</div>
    <div class="ttl" style="font-size:5.5px"><span>03.</span> Text Added Here</div>
    <div class="tx" style="margin-top:2px">Lorem ipsum dolor sit amet, consectetuer adipiscing elit, sed diam nonummy nibh euismod tincidunt ut laoreet dolore magna aliquam erat volutpat. Ut wisi enim ad minim veniam.</div>
  </div>
  <div class="footer">LUMORA</div><div class="footer-line"></div><div class="page-no">5</div>
</section>

<!-- Row 3 -->
<section class="slide list-spine" style="left:30px;top:360px">
  <div class="heading"><b>Heading</b> Goes Here</div><div class="corner-dot"></div>
  <div class="abs" style="left:29px;top:34px;width:92px">
    <div class="ttl"><span>01.</span> Aliquam Erat Volutpat</div><div class="tx" style="margin-bottom:9px">Lorem ipsum dolor sit amet, consectetuer adipiscing elit, sed diam nonummy nibh euismod.</div>
    <div class="ttl"><span>02.</span> Consectetuer Adipiscing Elit</div><div class="tx" style="margin-bottom:9px">Lorem ipsum dolor sit amet, consectetuer adipiscing elit, sed diam nonummy nibh euismod tincidunt ut laoreet.</div>
    <div class="ttl"><span>03.</span> Duis Autem Vel Eum</div><div class="tx" style="margin-bottom:9px">Lorem ipsum dolor sit amet, consectetuer adipiscing elit, sed diam nonummy nibh euismod tincidunt.</div>
    <div class="ttl"><span>04.</span> Aliquam Erat Volutpat</div><div class="tx">Lorem ipsum dolor sit amet, consectetuer adipiscing elit, sed diam nonummy nibh euismod tincidunt ut laoreet.</div>
  </div>
  <svg class="abs" style="left:0;top:0" width="265" height="149" viewBox="0 0 265 149">
    <rect x="141" y="25" width="6" height="107" fill="var(--navy)"/>
    <g fill="var(--green)" stroke="#fff" stroke-width="1.5"><circle cx="144" cy="49" r="11"/><circle cx="144" cy="78" r="11"/><circle cx="144" cy="109" r="11"/></g>
    <g fill="none" stroke="#fff" stroke-width=".9"><rect x="139" y="45" width="10" height="7"/><path d="M144 52v3M140 55h8M139 78a5 4 0 0 1 10 0zM144 78v5M139 113l3-6 4 4 3-5"/></g>
  </svg>
  <div class="abs" style="left:162px;top:43px;width:80px">
    <div class="ttl" style="font-size:5px">LOREM IPSUM</div><div class="tx" style="margin-bottom:13px">Ipsum dolor sit amet, cons ectetuer adipiscing elit, sed diam nonummy nibh euismod tincidunt ut laoreet</div>
    <div class="ttl" style="font-size:5px">LOREM IPSUM</div><div class="tx" style="margin-bottom:11px">Ipsum dolor sit amet, cons ectetuer adipiscing elit, sed diam nonummy nibh euismod tincidunt ut laoreet dolore magna aliquam erat volutpat.</div>
    <div class="ttl" style="font-size:5px">LOREM IPSUM</div><div class="tx">Ipsum dolor sit amet, cons ectetuer adipiscing elit, sed diam nonummy nibh euismod tincidunt</div>
  </div>
  <div class="footer">LUMORA</div><div class="footer-line"></div><div class="page-no">6</div>
</section>

<section class="slide section-divider" style="left:312px;top:360px">
  <div class="abs" style="left:0;top:0;width:265px;height:21px;background:var(--navy)"></div>
  <div class="abs" style="left:0;top:128px;width:265px;height:21px;background:var(--navy)"></div>
  <svg class="abs" style="left:0;top:0" width="265" height="149" viewBox="0 0 265 149">
    <circle cx="95" cy="77" r="30" fill="none" stroke="var(--blue)" stroke-width="6" stroke-dasharray="60 6 45 6 60 6" />
    <circle cx="95" cy="77" r="30" fill="none" stroke="var(--green)" stroke-width="6" stroke-dasharray="40 150" stroke-dashoffset="-110"/>
    <circle cx="95" cy="77" r="30" fill="none" stroke="var(--navy)" stroke-width="6" stroke-dasharray="35 155" stroke-dashoffset="-60"/>
    <text x="95" y="86" text-anchor="middle" font-family="Poppins, sans-serif" font-weight="800" font-size="24" fill="var(--navy)">01</text>
  </svg>
  <div class="abs" style="left:136px;top:64px;font-size:11px;font-weight:700;color:var(--navy)">Part One.</div>
  <div class="abs" style="left:136px;top:80px;width:80px;font-size:3.6px;line-height:1.4;color:#555">Lorem ipsumectetuer adipiscing elit sed diam nonummy nibh euismod tincidunt</div>
</section>

<section class="slide quad-grid" style="left:591px;top:360px">
  <div class="heading"><b>Heading</b> Goes Here</div><div class="corner-dot"></div>
  <div class="abs" style="left:20px;top:44px;width:60px"><div class="ttl"><span>01.</span> Project Problem</div><div class="tx">Lorem ipsum dolor sit amet, cons ectetuer adipiscing elit, sed diam nonummy nibh euismod tincidunt.</div></div>
  <div class="abs" style="left:20px;top:86px;width:60px"><div class="ttl"><span>03.</span> Project Market</div><div class="tx">Lorem ipsum dolor sit amet, cons ectetuer adipiscing elit, sed diam nonummy nibh euismod tincidunt.</div></div>
  <div class="abs" style="left:183px;top:44px;width:60px"><div class="ttl"><span>02.</span> Project Solution</div><div class="tx">Lorem ipsum dolor sit amet, cons ectetuer adipiscing elit, sed diam nonummy nibh euismod tincidunt.</div></div>
  <div class="abs" style="left:183px;top:86px;width:60px"><div class="ttl"><span>04.</span> Project Mission</div><div class="tx">Lorem ipsum dolor sit amet, cons ectetuer adipiscing elit, sed diam nonummy nibh euismod tincidunt.</div></div>
  <div class="abs" style="left:88px;top:35px;width:43px;height:40px;background:var(--green);padding:17px 5px 0;color:#fff"><div style="font-size:4px;font-weight:700">PROBLEM</div><div style="font-size:2.4px;line-height:1.4">Lorem ipsum dolor sit amet, cons ectetuer adipiscing elit.</div></div>
  <div class="abs" style="left:133px;top:35px;width:43px;height:40px;background:var(--navy);padding:17px 5px 0;color:#fff"><div style="font-size:4px;font-weight:700">SOLUTION</div><div style="font-size:2.4px;line-height:1.4">Lorem ipsum dolor sit amet, cons ectetuer adipiscing elit.</div></div>
  <div class="abs" style="left:88px;top:78px;width:43px;height:40px;background:var(--navy);padding:17px 5px 0;color:#fff"><div style="font-size:4px;font-weight:700">MARKET</div><div style="font-size:2.4px;line-height:1.4">Lorem ipsum dolor sit amet, cons ectetuer adipiscing elit.</div></div>
  <div class="abs" style="left:133px;top:78px;width:43px;height:40px;background:var(--green);padding:17px 5px 0;color:#fff"><div style="font-size:4px;font-weight:700">MISSION</div><div style="font-size:2.4px;line-height:1.4">Lorem ipsum dolor sit amet, cons ectetuer adipiscing elit.</div></div>
  <div class="footer">LUMORA</div><div class="footer-line"></div><div class="page-no">8</div>
</section>

<!-- Row 4 -->
<section class="slide chart" style="left:30px;top:523px">
  <div class="heading"><b>Heading</b> Goes Here</div><div class="corner-dot"></div>
  <svg class="abs" style="left:0;top:0" width="265" height="149" viewBox="0 0 265 149" font-family="Poppins, sans-serif">
    <g font-size="2.4" fill="#888" text-anchor="end"><text x="25" y="114">0</text><text x="25" y="102">1</text><text x="25" y="91">2</text><text x="25" y="79">3</text><text x="25" y="68">4</text><text x="25" y="56">5</text><text x="25" y="45">6</text></g>
    <line x1="28" y1="113" x2="128" y2="113" stroke="#ccc" stroke-width=".4"/>
    <g fill="var(--navy)"><rect x="33" y="58" width="6" height="55"/><rect x="67" y="58" width="6" height="55"/><rect x="100" y="55" width="6" height="58"/></g>
    <g fill="var(--green)"><rect x="40" y="68" width="6" height="45"/><rect x="74" y="35" width="6" height="78"/><rect x="107" y="73" width="6" height="40"/></g>
    <g fill="var(--blue)"><rect x="47" y="82" width="6" height="31"/><rect x="81" y="64" width="6" height="49"/><rect x="114" y="64" width="6" height="49"/></g>
    <g font-size="2.8" fill="#555" text-anchor="middle"><text x="43" y="119">Category 1</text><text x="77" y="119">Category 2</text><text x="110" y="119">Category 3</text></g>
    <g font-size="2" fill="#888"><circle cx="60" cy="124" r=".8" fill="var(--navy)"/><text x="62" y="124.7">Series 1</text><circle cx="72" cy="124" r=".8" fill="var(--green)"/><text x="74" y="124.7">Series 2</text><circle cx="84" cy="124" r=".8" fill="var(--blue)"/><text x="86" y="124.7">Series 3</text></g>
    <circle cx="149" cy="45" r="6" fill="var(--navy)"/><circle cx="149" cy="76" r="6" fill="var(--green)"/><circle cx="149" cy="108" r="6" fill="var(--blue)"/>
    <g fill="#fff" font-size="6" font-weight="700" text-anchor="middle"><text x="149" y="47">1</text><text x="149" y="78">2</text><text x="149" y="110">3</text></g>
  </svg>
  <div class="abs" style="left:162px;top:37px;width:80px"><div class="ttl" style="font-size:5px">Lorem ipsum dolor.</div><div class="tx">Lorem ipsumectetuer adipiscing elit, sed diam nonummy nibh euismod tincidunt sed diam nonummy nibhuit</div></div>
  <div class="abs" style="left:162px;top:68px;width:80px"><div class="ttl" style="font-size:5px"><span>Lorem ipsum dolor.</span></div><div class="tx">Lorem ipsumectetuer adipiscing elit, sed diam nonummy nibh euismod tincidunt sed diam nonummy nibhuit</div></div>
  <div class="abs" style="left:162px;top:100px;width:80px"><div class="ttl" style="font-size:5px;color:var(--blue)">Lorem ipsum dolor.</div><div class="tx">Lorem ipsumectetuer adipiscing elit, sed diam nonummy nibh euismod tincidunt sed diam nonummy nibhuit</div></div>
  <div class="footer">LUMORA</div><div class="footer-line"></div><div class="page-no">9</div>
</section>

<section class="slide four-cards" style="left:312px;top:523px">
  <div class="heading"><b>Heading</b> Goes Here</div><div class="corner-dot"></div>
  <svg class="abs" style="left:0;top:0" width="265" height="149" viewBox="0 0 265 149">
    <g fill="none" stroke="var(--navy)" stroke-width=".9"><path d="M43 43H37V100H80V43H74M93 43H87V100H130V43H124M144 43H138V100H181V43H175M194 43H188V100H231V43H225"/></g>
    <g fill="var(--green)" stroke="#fff" stroke-width="1"><circle cx="58.5" cy="43" r="7"/><circle cx="108.5" cy="43" r="7"/><circle cx="159.5" cy="43" r="7"/><circle cx="209.5" cy="43" r="7"/></g>
    <g fill="none" stroke="#fff" stroke-width=".7"><rect x="55" y="40" width="7" height="6"/><rect x="105" y="40" width="7" height="5"/><path d="M156 42l3.5-2 3.5 2-3.5 2z M206 40h7v5h-7z"/></g>
  </svg>
  <div class="abs" style="left:40px;top:54px;width:38px"><div class="ttl" style="color:var(--blue);font-size:3.6px">LOREM IPSUM</div><div class="tx">Lorem dolor sit amet, cons ectetuer adipiscing elit, sed diam nonummy nibh euismod tincidunt ut laoreet.</div></div>
  <div class="abs" style="left:90px;top:54px;width:38px"><div class="ttl" style="color:var(--blue);font-size:3.6px">LOREM IPSUM</div><div class="tx">Lorem dolor sit amet, cons ectetuer adipiscing elit, sed diam nonummy nibh euismod tincidunt ut laoreet.</div></div>
  <div class="abs" style="left:141px;top:54px;width:38px"><div class="ttl" style="color:var(--blue);font-size:3.6px">LOREM IPSUM</div><div class="tx">Lorem dolor sit amet, cons ectetuer adipiscing elit, sed diam nonummy nibh euismod tincidunt ut laoreet.</div></div>
  <div class="abs" style="left:191px;top:54px;width:38px"><div class="ttl" style="color:var(--blue);font-size:3.6px">LOREM IPSUM</div><div class="tx">Lorem dolor sit amet, cons ectetuer adipiscing elit, sed diam nonummy nibh euismod tincidunt ut laoreet.</div></div>
  <div class="abs" style="left:38px;top:106px;font-size:8px;font-weight:700;color:var(--navy)">+ 35k</div>
  <div class="abs tx" style="left:38px;top:117px;width:195px;color:#555">Lorem ipsum dolor sit amet, consectetuer adipiscing elit, sed diam nonummy nibh euismod tincidunt ut laoreet dolore magna aliquam erat volutpat. Ut wisi enim ad minim veniam.</div>
  <div class="footer">LUMORA</div><div class="footer-line"></div><div class="page-no">10</div>
</section>

<section class="slide feature" style="left:591px;top:523px">
  <div class="heading"><b>Heading</b> Goes Here</div><div class="corner-dot"></div>
  <div class="photo" role="img" aria-label="Hand holding a glowing medical shield over digital health graphics" style="left:21px;top:35px;width:128px;height:54px;border-radius:0;background:linear-gradient(120deg,#bfdcee,#e9f3f9 50%,#7fb6db)"></div>
  <div class="abs" style="left:156px;top:42px;font-size:11px;font-weight:700;color:var(--navy);line-height:1.05">Heading<br><span style="color:var(--green);font-weight:500;font-size:9.5px">Text Goes Here</span></div>
  <div class="abs" style="left:107px;top:73px;width:138px;height:51px;background:var(--navy)"></div>
  <div class="abs" style="left:155px;top:77px;font-size:7px;color:#fff;line-height:1">Text<br><span style="color:var(--green)">Added Here</span></div>
  <div class="abs" style="left:113px;top:98px;width:128px;font-size:2.6px;line-height:1.45;color:#dcdcef">Lorem ipsum dolor sit amet, consectetuer adipiscing elit, sed diam nonummy nibh euismod tincidunt ut laoreet dolore magna aliquam erat volutpat. Ut wisi enim ad minim veniam, quis nostrud exerci tation.</div>
  <div class="abs" style="left:26px;top:95px;font-size:6px;font-weight:700;line-height:1.3;color:var(--green)">Adipiscing Elit<br><span style="color:var(--navy)">Sed Diam Nonummy</span><br>Nibh Euismod</div>
  <div class="footer">LUMORA</div><div class="footer-line"></div><div class="page-no">11</div>
</section>

<!-- Row 5 -->
<section class="slide options" style="left:30px;top:687px">
  <div class="heading"><b>Heading</b> Goes Here</div><div class="corner-dot"></div>
  <svg class="abs" style="left:23px;top:60px" width="32" height="32" viewBox="0 0 32 32"><path d="M0 0H14L30 16L14 32H0L16 16Z" fill="#e6e6e8"/></svg>
  <div class="photo" role="img" aria-label="Nurse caring for an elderly patient" style="left:66px;top:33px;width:49px;height:58px;border-radius:0;background:linear-gradient(160deg,#7da6cf,#d9e4ee)"></div>
  <div class="photo" role="img" aria-label="Doctor in a mask examining a patient" style="left:130px;top:33px;width:49px;height:58px;border-radius:0;background:linear-gradient(160deg,#c9d6e0,#8a9bae)"></div>
  <div class="photo" role="img" aria-label="Lab scientist working with samples" style="left:193px;top:33px;width:49px;height:58px;border-radius:0;background:linear-gradient(160deg,#8fb9da,#e4edf4)"></div>
  <div class="abs" style="left:66px;top:95px;width:49px"><div style="font-size:4.5px;color:var(--navy)">First <b style="color:var(--blue)">Option</b></div><div class="tx">Lorem ipsum dolor sit consectetuer adipiscing elit, sed diam nonummy nibh euismod tincidunt.</div></div>
  <div class="abs" style="left:130px;top:95px;width:49px"><div style="font-size:4.5px;color:var(--navy)">Second <b style="color:var(--blue)">Option</b></div><div class="tx">Lorem ipsum dolor sit consectetuer adipiscing elit, sed diam nonummy nibh euismod tincidunt.</div></div>
  <div class="abs" style="left:193px;top:95px;width:49px"><div style="font-size:4.5px;color:var(--navy)">Third <b style="color:var(--blue)">Option</b></div><div class="tx">Lorem ipsum dolor sit consectetuer adipiscing elit, sed diam nonummy nibh euismod tincidunt.</div></div>
  <div class="footer">LUMORA</div><div class="footer-line"></div><div class="page-no">12</div>
</section>

<section class="slide text-photo" style="left:312px;top:687px">
  <div class="heading"><b>Heading</b> Goes Here</div><div class="corner-dot"></div>
  <div class="abs" style="left:21px;top:41px;font-size:8.5px;font-weight:700;color:var(--navy);line-height:1.2">Consectetuer<br><span style="color:var(--green)">Dipiscing Volutpat</span></div>
  <div class="abs tx" style="left:21px;top:64px;width:92px;color:#666">Lorem ipsum dolor sit amet, cons ectetuer adipiscing elit, sed diam nonummy nibh euismod tincidunt ut laoreet dolore magna aliquam erat volutpat. Ut wisi enim ad minim veniam, quis nostrud exerci tation ullamcorper suscipit lobortis nisl ut aliquip ex ea commodo consequat. Duis autem vel eum iriure dolor in hendrerit in vulputate velit esse molestie consequat.</div>
  <div class="photo" role="img" aria-label="Doctor touching a holographic medical scan display" style="left:128px;top:28px;width:113px;height:92px;border-radius:0;background:radial-gradient(circle at 40% 45%,#f2c9c3,#6ea3cc 45%,#2f5f8e)"></div>
  <div class="footer">LUMORA</div><div class="footer-line"></div><div class="page-no">13</div>
</section>

<section class="slide two-col" style="left:591px;top:687px">
  <div class="heading"><b>Heading</b> Goes Here</div><div class="corner-dot"></div>
  <div class="abs" style="left:24px;top:35px;width:104px"><div class="ttl" style="font-size:7px"><span>01.</span> Text Added Here</div><div class="tx" style="margin-top:3px">Lorem ipsum dolor sit amet, cons ectetuer adipiscing elit, sed diam nonummy nibh euismod tincidunt ut laoreet dolore magna aliquam erat volutpat. Ut wisi enim ad minim veniam, quis nostrud exerci tation ullamcorper suscipit lobortis nisl ut aliquip ex ea commodo consequat.<br><br>Lorem ipsum dolor sit amet, cons ectetuer adipiscing elit, sed diam nonummy nibh euismod tincidunt ut laoreet dolore magna aliquam erat volutpat.<br><br>Lorem ipsum dolor sit amet, consectetuer adipiscing elit, sed diam nonummy nibh euismod tincidunt ut laoreet dolore magna.</div></div>
  <div class="abs" style="left:139px;top:35px;width:104px"><div class="ttl" style="font-size:7px"><span>02.</span> Text Added Here</div><div class="tx" style="margin-top:3px">Lorem ipsum dolor sit amet, cons ectetuer adipiscing elit, sed diam nonummy nibh euismod tincidunt ut laoreet dolore magna aliquam erat volutpat. Ut wisi enim ad minim veniam, quis nostrud exerci tation ullamcorper suscipit lobortis nisl ut aliquip ex ea commodo consequat.<br><br>Lorem ipsum dolor sit amet, cons ectetuer adipiscing elit, sed diam nonummy nibh euismod tincidunt ut laoreet dolore magna aliquam erat volutpat.<br><br>Lorem ipsum dolor sit amet, consectetuer adipiscing elit, sed diam nonummy nibh euismod tincidunt ut laoreet dolore magna.</div></div>
  <div class="footer">LUMORA</div><div class="footer-line"></div><div class="page-no">14</div>
</section>

<!-- Row 6 -->
<section class="slide timeline" style="left:30px;top:852px">
  <div class="heading"><b>Heading</b> Goes Here</div><div class="corner-dot"></div>
  <svg class="abs" style="left:0;top:0" width="265" height="149" viewBox="0 0 265 149" font-family="Poppins, sans-serif">
    <g fill="var(--green)"><path d="M23 84L29 78H67L61 84Z"/><path d="M109 84L115 78H153L147 84Z"/><path d="M195 84L201 78H240L234 84Z"/></g>
    <g fill="var(--navy)"><path d="M66 84L72 78H110L104 84Z"/><path d="M152 84L158 78H196L190 84Z"/></g>
    <g fill="#fff" font-size="3.3" font-weight="600" text-anchor="middle"><text x="45" y="82.3">1990</text><text x="88" y="82.3">2001</text><text x="131" y="82.3">2007</text><text x="174" y="82.3">2012</text><text x="217" y="82.3">2020</text></g>
    <g stroke="var(--navy)" stroke-width=".7"><path d="M45 65V77M131 65V77M217 65V77M88 85V97M174 85V97"/></g>
    <g fill="var(--navy)"><circle cx="45" cy="64" r="1.3"/><circle cx="131" cy="64" r="1.3"/><circle cx="217" cy="64" r="1.3"/><circle cx="88" cy="98" r="1.3"/><circle cx="174" cy="98" r="1.3"/></g>
    <g text-anchor="middle">
      <g font-size="4" font-weight="700" fill="var(--navy)"><text x="45" y="44">YOUR TITLE</text><text x="131" y="44">YOUR TITLE</text><text x="217" y="44">YOUR TITLE</text><text x="88" y="108">YOUR TITLE</text><text x="174" y="108">YOUR TITLE</text></g>
      <g font-size="3" fill="#999"><text x="45" y="49">Refers to a good or</text><text x="45" y="53">service being offered</text><text x="131" y="49">Refers to a good or</text><text x="131" y="53">service being offered</text><text x="217" y="49">Refers to a good or</text><text x="217" y="53">service being offered</text><text x="88" y="113">Refers to a good or</text><text x="88" y="117">service being offered</text><text x="174" y="113">Refers to a good or</text><text x="174" y="117">service being offered</text></g>
    </g>
  </svg>
  <div class="footer">LUMORA</div><div class="footer-line"></div><div class="page-no">15</div>
</section>

<section class="slide cycle" style="left:312px;top:852px">
  <div class="heading"><b>Heading</b> Goes Here</div><div class="corner-dot"></div>
  <svg class="abs" style="left:0;top:0" width="265" height="149" viewBox="0 0 265 149" font-family="Poppins, sans-serif">
    <path d="M133 76V39A37 37 0 0 0 96 76Z" fill="var(--green)"/>
    <path d="M133 76V39A37 37 0 0 1 170 76Z" fill="var(--navy)"/>
    <path d="M133 76H96A37 37 0 0 0 133 113Z" fill="var(--navy)"/>
    <path d="M133 76H170A37 37 0 0 1 133 113Z" fill="var(--green)"/>
    <g stroke="#fff" stroke-width="1.2"><path d="M133 39V113M96 76H170"/></g>
    <circle cx="133" cy="76" r="19" fill="#fff"/>
    <g fill="none" stroke="#fff" stroke-width=".8"><circle cx="113" cy="57" r="3"/><path d="M151 60l4-5M150 55l5 0 0 5"/><rect x="110" y="92" width="6" height="6"/><circle cx="153" cy="95" r="3"/></g>
    <g font-size="6" font-weight="700" fill="var(--navy)" text-anchor="middle"><text x="133" y="75">Text</text><text x="133" y="82">Added</text></g>
    <g font-size="4.5" font-weight="700"><text x="87" y="43" text-anchor="end" fill="var(--navy)">Text Here</text><text x="177" y="43" fill="var(--green)">Text Here</text><text x="87" y="96" text-anchor="end" fill="var(--green)">Text Here</text><text x="177" y="96" fill="var(--navy)">Text Here</text></g>
  </svg>
  <div class="abs tx" style="left:28px;top:46px;width:59px;text-align:right">Lorem ipsum dolor sit amet, consectetuer adipiscing elit, sed diam nonummy nibh euismod tincidunt ut laoreet dolore</div>
  <div class="abs tx" style="left:177px;top:46px;width:59px">Lorem ipsum dolor sit amet, consectetuer adipiscing elit, sed diam nonummy nibh euismod tincidunt ut laoreet dolore</div>
  <div class="abs tx" style="left:28px;top:99px;width:59px;text-align:right">Lorem ipsum dolor sit amet, consectetuer adipiscing elit, sed diam nonummy nibh euismod tincidunt ut laoreet dolore</div>
  <div class="abs tx" style="left:177px;top:99px;width:59px">Lorem ipsum dolor sit amet, consectetuer adipiscing elit, sed diam nonummy nibh euismod tincidunt ut laoreet dolore</div>
  <div class="footer">LUMORA</div><div class="footer-line"></div><div class="page-no">16</div>
</section>

<section class="slide steps" style="left:591px;top:852px">
  <div class="heading"><b>Heading</b> Goes Here</div><div class="corner-dot"></div>
  <svg class="abs" style="left:0;top:0" width="265" height="149" viewBox="0 0 265 149" font-family="Poppins, sans-serif">
    <rect x="20" y="69" width="60" height="3.5" fill="var(--navy)"/><rect x="80" y="69" width="44" height="3.5" fill="var(--green)"/><rect x="124" y="69" width="44" height="3.5" fill="var(--navy)"/><rect x="168" y="69" width="72" height="3.5" fill="var(--green)"/>
    <path d="M240 66.5L245 70.7L240 75Z" fill="var(--green)"/>
    <g fill="none" stroke-width="3"><circle cx="63" cy="57" r="13" stroke="var(--navy)"/><circle cx="110" cy="57" r="13" stroke="var(--green)"/><circle cx="156" cy="57" r="13" stroke="var(--navy)"/><circle cx="203" cy="57" r="13" stroke="var(--green)"/></g>
    <g fill="var(--green)"><circle cx="63" cy="57" r="8"/><circle cx="156" cy="57" r="8"/></g>
    <g fill="var(--navy)"><circle cx="110" cy="57" r="8"/><circle cx="203" cy="57" r="8"/></g>
    <g fill="none" stroke="#fff" stroke-width=".8"><circle cx="63" cy="57" r="3.5"/><path d="M63 55v2h2"/><ellipse cx="156" cy="55" rx="3.5" ry="1.3"/><path d="M152.5 55v4a3.5 1.3 0 0 0 7 0v-4"/><circle cx="202" cy="56" r="2.5"/><path d="M204 58l2.5 2.5"/></g>
    <text x="110" y="59" font-size="5" font-weight="700" fill="#fff" text-anchor="middle">$</text>
    <g font-size="2.8" fill="#fff" font-weight="600" text-anchor="middle"><text x="73" y="72">Step 01</text><text x="120" y="72">Step 02</text><text x="166" y="72">Step 03</text><text x="222" y="72">Step 04</text></g>
    <g stroke="var(--navy)" stroke-width=".6"><path d="M63 77V84M110 77V84M156 77V84M203 77V84"/></g>
    <g font-size="4" font-weight="700" fill="var(--navy)" text-anchor="middle"><text x="63" y="91">LOREM IPSUM</text><text x="110" y="91">LOREM IPSUM</text><text x="156" y="91">LOREM IPSUM</text><text x="203" y="91">LOREM IPSUM</text></g>
  </svg>
  <div class="abs tx" style="left:46px;top:93px;width:34px;text-align:center">Lorem ipsum dolor sit amet, consectetuer adipiscing elit, sed diam nonummy nibh euismod tincidunt.</div>
  <div class="abs tx" style="left:93px;top:93px;width:34px;text-align:center">Lorem ipsum dolor sit amet, consectetuer adipiscing elit, sed diam nonummy nibh euismod tincidunt.</div>
  <div class="abs tx" style="left:139px;top:93px;width:34px;text-align:center">Lorem ipsum dolor sit amet, consectetuer adipiscing elit, sed diam nonummy nibh euismod tincidunt.</div>
  <div class="abs tx" style="left:186px;top:93px;width:34px;text-align:center">Lorem ipsum dolor sit amet, consectetuer adipiscing elit, sed diam nonummy nibh euismod tincidunt.</div>
  <div class="footer">LUMORA</div><div class="footer-line"></div><div class="page-no">17</div>
</section>

<!-- Row 7 -->
<section class="slide bullets" style="left:30px;top:1016px">
  <div class="heading"><b>Heading</b> Goes Here</div><div class="corner-dot"></div>
  <div class="abs" style="left:23px;top:33px;width:110px"><div class="ttl" style="font-size:5.5px"><span>01.</span> Text Added Here</div><div class="tx" style="margin-top:2px">Lorem ipsum dolor sit amet, cons ectetuer adipiscing elit, sed diam nonummy nibh euismod tincidunt ut laoreet dolore magna aliquam erat volutpat.<br><br>Lorem ipsum dolor sit amet, consectetuer adipiscing elit, sed diam nonummy nibh euismod tincidunt ut laoreet dolore magna aliquam.</div></div>
  <div class="abs" style="left:23px;top:86px;width:110px"><div class="ttl" style="font-size:5.5px"><span>02.</span> Text Added Here</div><div class="tx" style="margin-top:2px">Lorem ipsum dolor sit amet, cons ectetuer adipiscing elit, sed diam nonummy nibh euismod tincidunt ut laoreet dolore magna aliquam erat volutpat.<br><br>Lorem ipsum dolor sit amet, consectetuer adipiscing elit, sed diam nonummy nibh euismod tincidunt ut laoreet dolore magna aliquam.</div></div>
  <ul class="abs" style="left:145px;top:41px;list-style:none;font-size:5.5px;color:var(--navy);line-height:14.5px">
    <li><span style="color:var(--green)">•</span> Fits Your Business Or Products</li>
    <li><span style="color:var(--green)">•</span> Is Easy To Spell And Remember</li>
    <li><span style="color:var(--green)">•</span> Fits Your Business Or Products</li>
    <li><span style="color:var(--green)">•</span> Is Easy To Spell And Remember</li>
    <li><span style="color:var(--green)">•</span> Fits Your Business Or Products</li>
    <li><span style="color:var(--green)">•</span> Is Easy To Spell And Remember</li>
  </ul>
  <div class="footer">LUMORA</div><div class="footer-line"></div><div class="page-no">18</div>
</section>

<section class="slide team" style="left:312px;top:1016px">
  <div class="heading"><b>Heading</b> Goes Here</div><div class="corner-dot"></div>
  <div class="abs" style="left:24px;top:48px;width:39px;height:15px;background:var(--navy)"></div>
  <div class="abs" style="left:82px;top:48px;width:39px;height:15px;background:var(--green)"></div>
  <div class="abs" style="left:142px;top:48px;width:39px;height:15px;background:var(--navy)"></div>
  <div class="abs" style="left:202px;top:48px;width:39px;height:15px;background:var(--green)"></div>
  <div class="abs" role="img" aria-label="Team member portrait" style="left:32px;top:53px;width:22px;height:22px;border-radius:50%;border:1.5px solid #fff;background:linear-gradient(#c9b2a2,#8d7a6d)"></div>
  <div class="abs" role="img" aria-label="Team member portrait" style="left:90px;top:53px;width:22px;height:22px;border-radius:50%;border:1.5px solid #fff;background:linear-gradient(#b38f78,#5e4538)"></div>
  <div class="abs" role="img" aria-label="Team member portrait" style="left:150px;top:53px;width:22px;height:22px;border-radius:50%;border:1.5px solid #fff;background:linear-gradient(#c9b2a2,#8d7a6d)"></div>
  <div class="abs" role="img" aria-label="Team member portrait" style="left:210px;top:53px;width:22px;height:22px;border-radius:50%;border:1.5px solid #fff;background:linear-gradient(#b38f78,#5e4538)"></div>
  <div class="abs" style="left:18px;top:79px;width:50px;text-align:center"><div class="ttl">AARON HALE</div><div class="tx">Lorem ipsum dolor sit amet, cons ectetuer adipiscing elit, sed diam nonummy nibh euismod.</div></div>
  <div class="abs" style="left:76px;top:79px;width:50px;text-align:center"><div class="ttl">NORA QUINN</div><div class="tx">Lorem ipsum dolor sit amet, cons ectetuer adipiscing elit, sed diam nonummy nibh euismod.</div></div>
  <div class="abs" style="left:136px;top:79px;width:50px;text-align:center"><div class="ttl">AARON HALE</div><div class="tx">Lorem ipsum dolor sit amet, cons ectetuer adipiscing elit, sed diam nonummy nibh euismod.</div></div>
  <div class="abs" style="left:196px;top:79px;width:50px;text-align:center"><div class="ttl">NORA QUINN</div><div class="tx">Lorem ipsum dolor sit amet, cons ectetuer adipiscing elit, sed diam nonummy nibh euismod.</div></div>
  <div class="footer">LUMORA</div><div class="footer-line"></div><div class="page-no">19</div>
</section>

<section class="slide closing" style="left:591px;top:1016px;background:var(--navy)">
  <div class="abs" role="img" aria-label="Faint medical imaging scene in the background" style="left:0;top:0;width:265px;height:149px;background:radial-gradient(circle at 30% 40%,#2c2870,#1f1b5c 70%)"></div>
  <div class="abs" style="left:144px;top:31px;font-size:17px;font-weight:700;color:#fff">Thank You</div>
  <div class="abs" style="left:32px;top:62px;font-size:12px;font-weight:700;color:#fff;display:flex;align-items:center;gap:5px"><i style="display:inline-block;width:20px;height:20px;border-radius:50%;background:#fff"></i><span class="brand-name">LUMORA<small>MEDICAL IMAGING</small></span></div>
  <svg class="abs" style="left:144px;top:69px" width="12" height="60" viewBox="0 0 12 60">
    <path d="M1 2c1 4 4 7 7 8l1.5-1.5-2-2-1 1c-1-.5-2-1.5-2.5-2.5l1-1-2-2z" fill="#fff"/>
    <path d="M1 20l8 3-3 1-1 3z" fill="#fff"/>
    <path d="M1 41l4-3.5 4 3.5h-1.2v3.5H2.2V41z" fill="#fff"/>
    <path d="M11 1v9M11 18v9M11 36v9" stroke="#fff" stroke-width=".5"/>
  </svg>
  <div class="abs" style="left:160px;top:69px;font-size:4px;line-height:1.4;color:#fff">+1 555 0142 2210<br>+1 555 0142 2211</div>
  <div class="abs" style="left:160px;top:87px;font-size:4px;line-height:1.4;color:#fff">www.lumoraimaging.com<br>hello@lumoraimaging.com</div>
  <div class="abs" style="left:160px;top:104px;font-size:4px;line-height:1.4;color:#fff">1234 Street name, town/city,<br>state/country, post/zip 012345.</div>
</section>

</body>
</html>
```